Word Harbour Needs an eBook Cover Design!

I am currently writing a unit of work for the Australian Curriculum entitled 'Ash & Ember: A Reading of Echoes of Conflict' for Year 10 students. This package will have two publications - a Teacher Companion and a Student Workbook.
I need a cover designed for both the Teacher Companion and the Student Workbook. These need to be matching covers, however, I also need them to be distinctive in some way so that a person can tell the difference between the teacher's guide and the student book. As it is a unit on the topic of war, I need the covers to reflect this theme - but nothing too graphic!
This is taken from my unit introduction:
"Through studying a variety of poetry, short stories, visual texts, media and multi-media texts and non-fiction, students will explore the context of war and its relevant issues: patriotism, nationalism, love, honour, sacrifice, destruction, pity and despair.
The texts within this unit offer the ideal forum for exploring issues of war as they capture the intensity of emotion that war evokes and demonstrate the ways in which language can be used to communicate powerful ideas and shape audience responses."
The following need to be included on the Teacher Companion cover:
1. Title - Ash & Ember: A Reading of Echoes of Conflict
2. Year 10
3. Australian Curriculum
4. Teacher Companion
5. Company logo
6. Authors' names - Clara Wendt and Martin Wendt
The following need to be included on the Student Workbook cover:
2. Year 10
3. Australian Curriculum
4. Student Workbook
5. Company logo
This is the first of a series of similar products, so I am looking for the same person to design covers for all the Teacher Companion/Student Workbook sets. For this reason, I need the covers to be designed with a series or product line in mind - i.e. I'm looking to brand the series in a distinctive way.
I have attached my company logo. My website address is www.wordharbour.com.au
Target Market(s)
Australian high school English teachers
Industry/Entity Type
It Company
Look and feel
Each slider illustrates characteristics of the customer's brand and the style your logo design should communicate.

```html
<!DOCTYPE html>
<html lang="en">
<head>
<meta charset="utf-8">
<title>Ash &amp; Ember – Cover Set</title>
<link rel="stylesheet" href="https://fonts.googleapis.com/css2?family=Cinzel:wght@400;700&family=Arimo:ital,wght@1,700&display=swap">
<style>
  :root {
    --page-bg: #ffffff;
    --ink-white: #ffffff;
    --ink-black: #111111;
    --title-red: #e8141b;
    --logo-blue: #1f6fb0;
    --url-red: #d81f26;
    --url-blue: #2aa6e0;
    --band-black: #050508;
    --rule: rgba(255,255,255,0.75);
    --student-deep: #050a1e;
    --student-mid: #143a8a;
    --student-glow: #3f7ee0;
    --teacher-deep: #150406;
    --teacher-mid: #6e1a10;
    --teacher-glow: #d0481e;
  }
  * { margin: 0; padding: 0; box-sizing: border-box; }
  html, body { width: 1200px; height: 1000px; overflow: hidden; background: var(--page-bg); }
  body { position: relative; font-family: "Cinzel", serif; }

  .cover {
    position: absolute;
    width: 538px;
    height: 805px;
    overflow: hidden;
    box-shadow: 6px 6px 10px rgba(0,0,0,0.45);
    color: var(--ink-white);
  }
  .cover--student { left: 40px; top: 96px; }
  .cover--teacher { left: 629px; top: 100px; }

  .cover__art { position: absolute; inset: 0; }
  .cover--student .cover__art {
    background:
      radial-gradient(circle at 0% 52%, #cfe4ff 0 6%, #4d8fe0 14%, rgba(30,70,160,0) 26%),
      radial-gradient(ellipse at 55% 25%, var(--student-glow) 0%, rgba(20,58,138,0.6) 35%, rgba(5,10,30,0) 70%),
      linear-gradient(180deg, var(--student-mid) 0%, #0c1d4a 55%, var(--student-deep) 100%);
  }
  .cover--teacher .cover__art {
    background:
      radial-gradient(circle at 0% 52%, #f3c07a 0 5%, #c9461c 14%, rgba(110,26,16,0) 26%),
      radial-gradient(ellipse at 55% 25%, var(--teacher-glow) 0%, rgba(110,26,16,0.6) 35%, rgba(21,4,6,0) 70%),
      linear-gradient(180deg, var(--teacher-mid) 0%, #3a0c08 55%, var(--teacher-deep) 100%);
  }

  .cover__logo {
    position: absolute; left: 0; top: 0;
    width: 122px; height: 74px;
    background: var(--ink-white);
    display: flex; flex-direction: column; align-items: center; justify-content: center; gap: 6px;
  }
  .cover__logo-mark { width: 22px; height: 22px; background: var(--logo-blue); }
  .cover__logo-name { font-family: "Cinzel", serif; font-weight: 700; font-size: 13px; color: var(--logo-blue); }

  .cover__url {
    position: absolute; left: 131px; top: 5px;
    font-family: "Arimo", sans-serif; font-style: italic; font-weight: 700;
    font-size: 11px; letter-spacing: 1.5px; text-decoration: underline;
  }
  .cover--student .cover__url { color: var(--url-red); }
  .cover--teacher .cover__url { color: var(--url-blue); }

  .cover__authors {
    position: absolute; left: 0; right: 0; top: 178px; text-align: center;
    font-size: 20px; letter-spacing: 3px;
  }
  .cover__title {
    position: absolute; left: 0; right: 0; top: 258px; text-align: center;
    font-size: 46px; font-weight: 400; line-height: 1;
  }
  .cover__title-accent { color: var(--title-red); }
  .cover__rule { position: absolute; left: 52px; right: 36px; height: 1px; background: var(--rule); }
  .cover__rule--upper { top: 331px; }
  .cover__rule--lower { top: 389px; }
  .cover__subtitle {
    position: absolute; left: 0; right: 0; top: 344px; text-align: center;
    font-size: 27px; white-space: nowrap;
  }

  .cover__year {
    position: absolute; right: 22px; top: 630px; width: 20px;
    display: flex; flex-direction: column; align-items: center;
    font-size: 19px; line-height: 29px;
  }

  .cover__edition {
    position: absolute; left: 0; top: 697px; width: 418px; height: 55px;
    background: var(--ink-white); color: var(--ink-black);
    font-size: 31px; display: flex; align-items: center; padding-left: 16px;
  }
  .cover__curriculum {
    position: absolute; left: 0; right: 58px; bottom: 0; height: 53px;
    background: var(--band-black);
    font-size: 25px; display: flex; align-items: center; padding-left: 16px;
  }
</style>
</head>
<body>

<section class="cover cover--student">
  <div class="cover__art" role="img" aria-label="Starry blue night sky with the Earth at the left edge, smoke clouds, marching soldier silhouettes and a couple holding hands"></div>
  <div class="cover__logo"><span class="cover__logo-mark"></span><span class="cover__logo-name">Word Harbour</span></div>
  <div class="cover__url">www.wordharbour.com.au</div>
  <p class="cover__authors">CLARA WENDT &amp; MARTIN WENDT</p>
  <h1 class="cover__title"><span class="cover__title-accent">ASH</span> &amp; EMBER:</h1>
  <div class="cover__rule cover__rule--upper"></div>
  <p class="cover__subtitle">A READING OF ECHOES OF CONFLICT</p>
  <div class="cover__rule cover__rule--lower"></div>
  <div class="cover__year"><span>Y</span><span>E</span><span>A</span><span>R</span><span>10</span></div>
  <div class="cover__edition">STUDENT WORKBOOK</div>
  <div class="cover__curriculum">AUSTRALIAN CURRICULUM</div>
</section>

<section class="cover cover--teacher">
  <div class="cover__art" role="img" aria-label="Fiery red night sky with the Earth and a glowing moon at the left, smoke clouds, marching soldier silhouettes and a couple holding hands"></div>
  <div class="cover__logo"><span class="cover__logo-mark"></span><span class="cover__logo-name">Word Harbour</span></div>
  <div class="cover__url">www.wordharbour.com.au</div>
  <p class="cover__authors">CLARA WENDT &amp; MARTIN WENDT</p>
  <h1 class="cover__title"><span class="cover__title-accent">ASH</span> &amp; EMBER:</h1>
  <div class="cover__rule cover__rule--upper"></div>
  <p class="cover__subtitle">A READING OF ECHOES OF CONFLICT</p>
  <div class="cover__rule cover__rule--lower"></div>
  <div class="cover__year"><span>Y</span><span>E</span><span>A</span><span>R</span><span>10</span></div>
  <div class="cover__edition">TEACHER COMPANION</div>
  <div class="cover__curriculum">AUSTRALIAN CURRICULUM</div>
</section>

</body>
</html>
```